Etiketten-Design für Gin- und Rumhersteller
Zielgruppe
Zielgruppe 20-35 Jahre, Wir sind ein Gin- und Rumhersteller und hätten gerne ein Etikett für unsere Flaschen. Etikett-Maße jeweils 70 x 70 mm.
Aufgabenstellung
Schwarzweißes Design, eventuell mit Gold oder Silber, Etikett selbst schwarz. Junger moderner Stil, Das Logo soll Groß auf dem Etikett sichtbar sein. Es gibt nur eine Vorderseite. Maße 70 x 70 mm.
Etikett Aufbau :
Wolkenhof (Groß, Logo anbei)
GIN oder RUM
40% Alk
hergestellt & abgefüllt in Vorarlberg
Wolkenhof Gin
aus der Firmengruppe der
HausKontor (Klein, Logo anbei)

```html
<!DOCTYPE html>
<html lang="de">
<head>
<meta charset="utf-8">
<title>Wolkenhof – Etiketten Gin &amp; Rum</title>
<link rel="stylesheet" href="https://fonts.googleapis.com/css2?family=Cormorant+Garamond:wght@500;600&family=Montserrat:wght@200;300;400&family=Roboto+Condensed:wght@300;400;700&display=swap">
<style>
  :root {
    --page: #ffffff;
    --label-dark: #14151c;
    --label-mid: #262834;
    --label-sheen: #2f3140;
    --ink: #ffffff;
    --ink-soft: #e6e6ea;
    --gold-dark: #9c7a3c;
    --gold: #d9b46a;
    --gold-light: #f5e3b5;
    --motif: rgba(255,255,255,0.035);
  }
  * { margin: 0; padding: 0; box-sizing: border-box; }
  html, body { width: 831px; height: 1200px; overflow: hidden; background: var(--page); }
  .sheet { position: relative; width: 831px; height: 1200px; }

  .label {
    position: absolute; left: 165px; width: 500px; height: 500px;
    background:
      linear-gradient(100deg, var(--label-dark) 0%, var(--label-mid) 22%, var(--label-sheen) 30%, var(--label-mid) 45%, var(--label-dark) 75%, var(--label-mid) 100%);
    overflow: hidden;
  }
  .label--gin { top: 70px; }
  .label--rum { top: 630px; }

  .label__motif {
    position: absolute; left: 150px; top: 40px; width: 300px; height: 340px;
    background: radial-gradient(ellipse at center, var(--motif) 0%, rgba(255,255,255,0) 70%);
  }

  .wordmark {
    position: absolute; left: 30px; top: 30px; height: 440px; width: 100px;
    writing-mode: vertical-rl; transform: rotate(180deg);
    display: flex; align-items: center; justify-content: center;
    font-family: "Cormorant Garamond", serif; font-weight: 600;
    font-size: 92px; line-height: 1; color: var(--ink); letter-spacing: 1px;
  }

  .rule {
    position: absolute; height: 2px;
    background: linear-gradient(90deg, var(--gold-dark), var(--gold-light) 50%, var(--gold-dark));
  }
  .rule--top { left: 166px; top: 50px; width: 270px; }
  .rule--mid { left: 165px; top: 256px; width: 240px; }
  .rule--bottom { left: 165px; top: 378px; width: 272px; }

  .product {
    position: absolute; left: 160px; top: 92px; width: 280px; height: 110px;
    display: flex; align-items: flex-end; justify-content: space-between;
    color: var(--ink); line-height: 1;
  }
  .product--gin { font-family: "Cormorant Garamond", serif; font-weight: 500; font-size: 124px; }
  .product--rum { font-family: "Montserrat", sans-serif; font-weight: 200; font-size: 116px; }

  .seal {
    position: absolute; left: 398px; top: 226px; width: 88px; height: 88px; border-radius: 50%;
    background: radial-gradient(circle at 40% 35%, var(--gold-light) 0%, var(--gold) 55%, var(--gold-dark) 100%);
  }

  .origin {
    position: absolute; left: 165px; top: 336px; width: 274px;
    font-family: "Roboto Condensed", sans-serif; font-weight: 300;
    font-size: 19.5px; color: var(--ink-soft); white-space: nowrap; letter-spacing: 0.2px;
  }

  .group {
    position: absolute; left: 162px; top: 433px; color: var(--ink);
    font-family: "Roboto Condensed", sans-serif;
  }
  .group__intro { font-size: 11px; font-weight: 300; display: block; }
  .group__name { font-size: 18px; font-weight: 700; display: flex; align-items: center; gap: 3px; margin-top: 1px; }
  .group__dot { width: 8px; height: 8px; border-radius: 50%; background: var(--ink); display: inline-block; }

  .strength {
    position: absolute; right: 62px; top: 442px;
    font-family: "Montserrat", sans-serif; font-weight: 300; color: var(--ink); white-space: nowrap;
  }
  .strength__value { font-size: 30px; }
  .strength__unit { font-size: 19px; font-weight: 400; }
</style>
</head>
<body>
<main class="sheet">

  <section class="label label--gin">
    <div class="label__motif" role="img" aria-label="Dezente Wacholderzweig-Illustration im Hintergrund"></div>
    <div class="wordmark">Wolkenhof</div>
    <div class="rule rule--top"></div>
    <h1 class="product product--gin"><span>G</span><span>I</span><span>N</span></h1>
    <div class="rule rule--mid"></div>
    <div class="seal" aria-hidden="true"></div>
    <p class="origin">Hergestellt &amp; abgefüllt in Vorarlberg</p>
    <div class="rule rule--bottom"></div>
    <p class="group"><span class="group__intro">Aus der Firmengruppe der</span><span class="group__name">HausKontor<span class="group__dot"></span></span></p>
    <p class="strength"><span class="strength__value">40%</span> <span class="strength__unit">Alk</span></p>
  </section>

  <section class="label label--rum">
    <div class="label__motif" role="img" aria-label="Dezente ornamentale Rum-Illustration im Hintergrund"></div>
    <div class="wordmark">Wolkenhof</div>
    <div class="rule rule--top"></div>
    <h1 class="product product--rum"><span>R</span><span>U</span><span>M</span></h1>
    <div class="rule rule--mid"></div>
    <div class="seal" aria-hidden="true"></div>
    <p class="origin">Hergestellt &amp; abgefüllt in Vorarlberg</p>
    <div class="rule rule--bottom"></div>
    <p class="group"><span class="group__intro">Aus der Firmengruppe der</span><span class="group__name">HausKontor<span class="group__dot"></span></span></p>
    <p class="strength"><span class="strength__value">40%</span> <span class="strength__unit">Alk</span></p>
  </section>

</main>
</body>
</html>
```